Vostra new design for business cards we want to change our existing design. Logo must remain the same

Hello we are the company VoSTra and offer various services regarding transportation and disposal. In addition to our main acquisition of van rental, we also offer disposal and express transportation, so we need new business card designs for our business. Our elders have their time and do not like it anymore. We want to change our existing design. Logo must remain the same as well as the color blue, whether dark or light Does not play a big role in the best medium blue. Logo must be present on the front side. As well as telephone, email, web and location. Big enough but not too big. Back can be redesigned Logo as well as name VoSTra must be present. Important is the text: Van rental Disposal and clearing express transportation. Without bail in red should be noted somewhere. it should be modern but not too playful. rather serious but no beating company Thank you very much

Target Market(s)

Private customers as well as companies we want to change our existing design. Logo must remain the same as well as the color blue, whether dark or light Does not play a big role in the best medium blue. Logo must be present on the front side. As well as telephone, email, web and location. Big enough but not too big. Back can be redesigned Logo as well as name VoSTra must be present. Important is the text: Van rental Disposal and clearing express transportation. Without bail in red should be noted somewhere. it should be modern but not too playful. rather serious but no beating company Thank you very much

Industry/Entity Type

Car Rental

Contact Information for Business Card

we want to change our existing design. Logo must remain the same as well as the color blue, whether dark or light Does not play a big role in the best medium blue.
Logo must be present on the front side.
As well as telephone, email, web and location. Big enough but not too big.
Back can be redesigned Logo as well as name VoSTra must be present.
Important is the text:
Van rental
Disposal and clearing
Express transportation.
Without bail in red should be noted somewhere.
it should be modern but not too playful. rather serious but no beating company
Thank you very much

Font styles to use
Sans Serif

Colors
33a6d7
ec1f27
0692cd
3277b5

Requirements
Must have
• logo and name VoSTra as described in the above text must have it. we want to change our existing design. Logo must remain the same as well as the color blue, whether dark or light Does not play a big role in the best medium blue. Logo must be present on the front side. As well as telephone, email, web and location. Big enough but not too big. Back can be redesigned Logo as well as name VoSTra must be present. Important is the text: Van rental Disposal and clearing express transportation. Without bail in red should be noted somewhere. it should be modern but not too playful. rather serious but no beating company Thank you very much
Nice to have
• see description we want to change our existing design. Logo must remain the same as well as the color blue, whether dark or light Does not play a big role in the best medium blue. Logo must be present on the front side. As well as telephone, email, web and location. Big enough but not too big. Back can be redesigned Logo as well as name VoSTra must be present. Important is the text: Van rental Disposal and clearing express transportation. Without bail in red should be noted somewhere. it should be modern but not too playful. rather serious but no beating company Thank you very much
Should not have
• Blue White and little red we want to change our existing design. Logo must remain the same as well as the color blue, whether dark or light Does not play a big role in the best medium blue. Logo must be present on the front side. As well as telephone, email, web and location. Big enough but not too big. Back can be redesigned Logo as well as name VoSTra must be present. Important is the text: Van rental Disposal and clearing express transportation. Without bail in red should be noted somewhere. it should be modern but not too playful. rather serious but no beating company Thank you very much

```html
<!DOCTYPE html>
<html lang="en">
<head>
<meta charset="utf-8">
<title>Vostra GmbH – Business Cards</title>
<link rel="stylesheet" href="https://fonts.googleapis.com/css2?family=Roboto:wght@400;500;700;900&display=swap">
<style>
  :root {
    --stage: #3a3a3c;
    --card-blue: #4b6597;
    --navy: #15137a;
    --white: #ffffff;
    --paper: #fbfbfd;
    --icon: #b9c4d9;
    --alert-red: #e8121c;
    --rule: rgba(255,255,255,0.85);
  }
  * { margin: 0; padding: 0; box-sizing: border-box; }
  html, body {
    width: 1200px; height: 1000px; overflow: hidden;
    background: var(--stage);
    font-family: "Roboto", Arial, sans-serif;
  }
  .card {
    position: absolute; left: 240px;
    width: 720px; height: 400px;
    border-radius: 28px; overflow: hidden;
    box-shadow: 0 14px 30px rgba(0,0,0,0.45);
  }

  /* ---------- back card ---------- */
  .card--back { top: 70px; background: var(--card-blue); }
  .brand { position: absolute; display: flex; align-items: center; }
  .brand__square { display: block; }
  .brand__name { font-weight: 900; line-height: 1; letter-spacing: 2px; }
  .card--back .brand { left: 150px; top: 62px; gap: 22px; }
  .card--back .brand__square { width: 70px; height: 70px; background: var(--white); }
  .card--back .brand__name { font-size: 78px; color: var(--white); }

  .services {
    position: absolute; left: 90px; right: 50px; top: 186px;
    border-top: 2px solid var(--rule);
    border-bottom: 2px solid var(--rule);
    padding: 14px 0 15px;
    color: var(--white); font-size: 15px; font-weight: 500;
    letter-spacing: 0.6px; text-transform: uppercase;
    display: flex; justify-content: space-between; align-items: center;
    white-space: nowrap; line-height: 1;
  }
  .services__item { flex: none; }
  .services__sep { flex: none; opacity: 0.9; padding: 0 10px; }

  .bail-band {
    position: absolute; left: 0; right: 0; top: 300px; height: 52px;
    background: var(--white);
    display: flex; align-items: center; justify-content: center;
  }
  .bail-band__label {
    color: var(--alert-red); font-weight: 900; font-size: 16px; letter-spacing: 0.5px;
    line-height: 1;
  }

  /* ---------- front card ---------- */
  .card--front { top: 530px; background: var(--paper); }
  .card--front .brand { left: 110px; top: 62px; gap: 26px; }
  .card--front .brand__square { width: 92px; height: 92px; background: var(--navy); }
  .card--front .brand__name { font-size: 96px; color: var(--navy); }

  .contact-panel {
    position: absolute; left: 0; right: 0; top: 212px; bottom: 0;
    background: var(--card-blue);
    border-top: 6px solid var(--navy);
  }
  .contact-list { position: absolute; list-style: none; }
  .contact-list--location { left: 60px; top: 38px; }
  .contact-list--online { left: 430px; top: 100px; }
  .contact-item {
    display: flex; align-items: center; gap: 12px;
    color: var(--white); font-size: 24px; font-weight: 500;
    margin-bottom: 10px; white-space: nowrap;
  }
  .contact-item svg { width: 22px; height: 22px; flex: none; }
</style>
</head>
<body>

<section class="card card--back" aria-label="Business card back">
  <div class="brand">
    <span class="brand__square"></span>
    <span class="brand__name">VOSTRA</span>
  </div>
  <p class="services">
    <span class="services__item">Van rental</span><span class="services__sep">|</span>
    <span class="services__item">Disposal and clearing</span><span class="services__sep">|</span>
    <span class="services__item">Express transportation</span>
  </p>
  <div class="bail-band">
    <span class="bail-band__label">WITHOUT BAIL</span>
  </div>
</section>

<section class="card card--front" aria-label="Business card front">
  <div class="brand">
    <span class="brand__square"></span>
    <span class="brand__name">VOSTRA</span>
  </div>

  <div class="contact-panel">
    <ul class="contact-list contact-list--location">
      <li class="contact-item">
        <svg viewBox="0 0 24 24" aria-hidden="true"><path fill="var(--icon)" d="M12 2a7 7 0 0 0-7 7c0 5 7 13 7 13s7-8 7-13a7 7 0 0 0-7-7zm0 9.5A2.5 2.5 0 1 1 12 6.5a2.5 2.5 0 0 1 0 5z"/></svg>
        Werkstrasse 14, 8500 Frauenfeld
      </li>
      <li class="contact-item">
        <svg viewBox="0 0 24 24" aria-hidden="true"><path fill="var(--icon)" d="M6.6 10.8a15.1 15.1 0 0 0 6.6 6.6l2.2-2.2a1 1 0 0 1 1-.25 11.4 11.4 0 0 0 3.6.57 1 1 0 0 1 1 1V20a1 1 0 0 1-1 1A17 17 0 0 1 3 4a1 1 0 0 1 1-1h3.5a1 1 0 0 1 1 1c0 1.25.2 2.450.57 3.57a1 1 0 0 1-.25 1z"/></svg>
        +41 70 555 00 00
      </li>
    </ul>

    <ul class="contact-list contact-list--online">
      <li class="contact-item">
        <svg viewBox="0 0 24 24" aria-hidden="true"><rect x="2" y="5" width="20" height="14" rx="2" fill="var(--icon)"/><path d="M3 6l9 7 9-7" fill="none" stroke="var(--card-blue)" stroke-width="1.8"/></svg>
        info@vostra.ch
      </li>
      <li class="contact-item">
        <svg viewBox="0 0 24 24" aria-hidden="true"><g fill="none" stroke="var(--icon)" stroke-width="1.8"><circle cx="12" cy="12" r="9"/><ellipse cx="12" cy="12" rx="4" ry="9"/><path d="M3 12h18M5 7h14M5 17h14"/></g></svg>
        www.VoSTra.ch
      </li>
    </ul>
  </div>
</section>

</body>
</html>
```